Brochure Design Project

Our company is KMV Sable Ridge. (no LOGO)

We are a restaurant marketing and advertising service. We market restaurants menus by producing a menu guide, distributing flyers and post cards, and also placing the restaurants menu on our website for delivery.

We make restaurants more profitable, by making their food more accessible. Marketing restaurants on search engines, websites, plazanet, wunq, zintro, and a total of 21 different marketing techniques that make restaurants more money.

Key Point: This is all done at NO COST to the restaurant.

We are looking for a design for a brochure that will be mailed as well as handed to restaurateurs.

In my attached file I am including our sales letter. The letter can stay in letter form for the inside of a tri-fold brochure or it can be part of your design.

For more information about our service, please read the attached sales letter.
Updates

Target Market(s)

Restaurant Owners and General managers

Industry/Entity Type

Advertising

Requirements
Must have
• Must look attractive and Eye-catching

```html
<!DOCTYPE html>
<html lang="en">
<head>
<meta charset="utf-8">
<title>KMV Sable Ridge – Tri-fold Brochure</title>
<link href="https://fonts.googleapis.com/css2?family=Roboto+Condensed:wght@400;700&family=Open+Sans:wght@400;600;700&display=swap" rel="stylesheet">
<style>
  :root {
    --paper: #dde2de;
    --teal: #5e8c80;
    --slate: #5f5f60;
    --ink: #222222;
    --body-ink: #3a3a3a;
    --navy: #1c3566;
    --divider: #8d918e;
    --white: #ffffff;
  }
  html, body {
    margin: 0;
    padding: 0;
    width: 1200px;
    height: 908px;
    overflow: hidden;
    background: var(--paper);
  }
  .brochure {
    position: relative;
    width: 1200px;
    height: 908px;
    background: var(--paper);
    font-family: "Open Sans", Arial, sans-serif;
    color: var(--ink);
  }
  .artwork {
    position: absolute;
    inset: 0;
  }
  .panel-divider {
    position: absolute;
    top: 0;
    width: 1px;
    height: 908px;
    background: var(--divider);
  }
  .heading {
    position: absolute;
    margin: 0;
    font-family: "Roboto Condensed", "Arial Narrow", sans-serif;
    font-weight: 400;
    color: var(--ink);
  }
  .about-heading { left: 35px; top: 40px; font-size: 31px; }
  .about-copy {
    position: absolute;
    left: 35px; top: 88px; width: 330px;
    margin: 0;
    font-size: 16.5px;
    line-height: 30.5px;
    letter-spacing: 0.4px;
    color: var(--body-ink);
  }
  .cost-callout {
    position: absolute;
    left: 15px; top: 366px; width: 361px;
    margin: 0;
    text-align: center;
    font-family: "Roboto Condensed", "Arial Narrow", sans-serif;
    font-size: 31px;
    line-height: 38px;
    color: var(--white);
  }
  .reach-heading { left: 432px; top: 40px; font-size: 31px; line-height: 35px; }
  .reach-copy {
    position: absolute;
    left: 432px; top: 124px; width: 334px;
    margin: 0;
    font-size: 13.5px;
    line-height: 27px;
    text-align: justify;
    letter-spacing: 0.3px;
    color: var(--body-ink);
  }
  .consult {
    position: absolute;
    left: 420px; top: 497px; width: 374px;
    margin: 0;
    text-align: center;
    font-size: 16.5px;
    line-height: 33.5px;
    color: var(--ink);
  }
  .contact {
    position: absolute;
    left: 420px; top: 663px; width: 374px;
    margin: 0;
    text-align: center;
    font-size: 17.5px;
    line-height: 31px;
    font-weight: 600;
    letter-spacing: 0.6px;
    color: #3d3d3d;
  }
  .contact .call { color: var(--navy); font-weight: 700; }
  .follow {
    position: absolute;
    left: 470px; top: 808px;
    display: flex;
    align-items: center;
    gap: 10px;
    font-family: "Roboto Condensed", "Arial Narrow", sans-serif;
    font-size: 16px;
    color: var(--ink);
  }
  .social {
    display: flex;
    align-items: center;
    gap: 5px;
    font-family: "Roboto Condensed", "Arial Narrow", sans-serif;
    font-size: 16px;
    color: var(--navy);
  }
  .social .mark {
    width: 14px; height: 14px;
    background: var(--navy);
  }
  .brand-name {
    position: absolute;
    left: 800px; top: 630px; width: 400px;
    margin: 0;
    text-align: center;
    font-family: "Open Sans", Arial, sans-serif;
    font-weight: 400;
    font-size: 39px;
    letter-spacing: -0.5px;
    color: var(--ink);
  }
  .tagline {
    position: absolute;
    left: 820px; top: 722px; width: 360px;
    margin: 0;
    text-align: center;
    font-family: "Roboto Condensed", "Arial Narrow", sans-serif;
    font-size: 26px;
    line-height: 32.5px;
    color: var(--ink);
  }
</style>
</head>
<body>
<main class="brochure">
  <svg class="artwork" width="1200" height="908" viewBox="0 0 1200 908" xmlns="http://www.w3.org/2000/svg">
    <defs>
      <linearGradient id="food-tones" x1="0" y1="0" x2="1" y2="1">
        <stop offset="0" stop-color="#3b2a22"/>
        <stop offset="0.35" stop-color="#c9553a"/>
        <stop offset="0.6" stop-color="#e9e4df"/>
        <stop offset="0.8" stop-color="#5d8a3a"/>
        <stop offset="1" stop-color="#b44a30"/>
      </linearGradient>
      <linearGradient id="city-tones" x1="0" y1="0" x2="0" y2="1">
        <stop offset="0" stop-color="#4a4a4c"/>
        <stop offset="0.45" stop-color="#8aa9c8"/>
        <stop offset="0.75" stop-color="#2f6fa8"/>
        <stop offset="1" stop-color="#1a1a1a"/>
      </linearGradient>
    </defs>

    <polygon class="food-photo" role="img" aria-label="Photo of many plates of stir-fried restaurant dishes on a table"
      points="0,523 131,617 400,499 400,908 0,908" fill="url(#food-tones)"/>

    <polygon class="city-illustration" role="img" aria-label="Illustration of city skyscrapers with direction signs and a crowd of business people"
      points="800,0 1200,0 1200,445 1007,548 800,412" fill="url(#city-tones)"/>

    <polygon class="zigzag-band"
      points="0,478 131,572 678,332 1007,548 1200,445 1200,494 1007,595 678,377 131,617 0,523"
      fill="var(--teal)"/>

    <rect class="accent-rule" x="17" y="330" width="355" height="6" fill="var(--teal)"/>
    <polygon class="cost-chevron" points="15,351 376,351 376,445 131,548 15,480" fill="var(--slate)"/>

    <polygon class="footer-chevron"
      points="601,908 827,823 1159,908 1088,908 851,854 662,908" fill="var(--slate)"/>
  </svg>

  <div class="panel-divider" style="left:400px"></div>
  <div class="panel-divider" style="left:800px"></div>

  <h2 class="heading about-heading">ABOUT US</h2>
  <p class="about-copy">KMV Sable Ridge is a restaurant marketing and advertising service that specializes in delivery. We deliver food from a variety of restaurants to people at their homes, offices or hotel rooms.</p>
  <p class="cost-callout">This is all done at NO COST<br>to the restaurant.</p>

  <h2 class="heading reach-heading">Reach More Potential<br>Customers!</h2>
  <p class="reach-copy">Your customers are searching your business and making their decisions online more than ever. KMV Sable Ridge helps you reach thousands of potential customers on search engines and social media platforms. We manage online advertising so you don't miss out on any additional business.</p>

  <p class="consult">To schedule a 15 min<br>consultation that is guaranteed to<br>NOT cost you anything and only make<br>your restaurant money.</p>

  <p class="contact"><span class="call">Call Nora Vestal Now</span><br>555-014-2876<br>or Visit<br>www.kmvsableridge.com</p>

  <div class="follow">
    <span>Follow us</span>
    <span class="social"><span class="mark"></span>plazanet</span>
    <span class="social"><span class="mark"></span>chirpline</span>
  </div>

  <h1 class="brand-name">KMV Sable Ridge</h1>
  <p class="tagline">We make Restaurants more profitable, by Making their food more accessible!</p>
</main>
</body>
</html>
```